Small boutique multi-family apartment developer needs premium website design.

We are a growing real estate development company specializing in multi family apartment development. Our company Mireval Stone Development focuses on passive real estate investors looking to maximize their current real estate portfolio by allowing us to develop and reposition their current properties allowing them more cashflow while we are also able to take over the management of their asset in order to ensure optimal performance on a consistent basis.

```html
<!DOCTYPE html>
<html lang="en">
<head>
<meta charset="utf-8">
<title>Mireval Stone Development</title>
<link href="https://fonts.googleapis.com/css2?family=Poppins:wght@300;400;500;600&display=swap" rel="stylesheet">
<style>
:root{
  --navy:#252c3a;
  --navy-deep:#1f2531;
  --rose:#c4aeb0;
  --rose-label:#bf9fa3;
  --mist:#eceef1;
  --ink:#2b2f38;
  --muted:#6b6f78;
  --white:#ffffff;
  --line:#c9ccd2;
}
*{margin:0;padding:0;box-sizing:border-box}
html,body{width:1200px;height:3755px;overflow:hidden;background:var(--white)}
body{font-family:'Poppins',sans-serif;color:var(--ink);position:relative}
.abs{position:absolute}
.photo{position:absolute}
.btn{position:absolute;display:flex;align-items:center;justify-content:center;font-size:10px;font-weight:500;letter-spacing:.5px;text-transform:uppercase;color:var(--white);background:var(--navy)}
.btn::before{content:"";position:absolute;left:0;top:50%;width:18px;height:2px;background:currentColor}
.btn.light{background:var(--white);color:var(--navy)}
.btn.sand{background:#c9b1ae;color:var(--navy)}

/* hero */
.hero{left:0;top:0;width:1200px;height:551px;background:linear-gradient(90deg,#1c222c 0%,#2f3642 40%,#5a4a3a 65%,#33373d 100%)}
.hero-shade{left:0;top:0;width:1200px;height:551px;background:linear-gradient(90deg,rgba(20,24,32,.75),rgba(20,24,32,.15) 70%)}
.logo{display:flex;align-items:center;gap:12px;color:var(--white);font-size:16px;font-weight:400}
.logo-mark{width:26px;height:26px;border:2px solid var(--white)}
.nav{top:28px;left:622px;display:flex;gap:52px;font-size:12px;color:var(--white)}
.nav .active{color:#d9b8b3}
.contact-btn{left:968px;top:21px;width:108px;height:32px;border:2px solid var(--white);background:transparent;font-size:10px}
.welcome{left:122px;top:168px;font-size:15px;color:var(--white);display:flex;align-items:center;gap:10px}
.welcome::after{content:"";width:60px;height:2px;background:var(--white)}
.hero-title{left:118px;top:196px;font-size:58px;line-height:61px;font-weight:400;color:var(--white)}
.hero-text{left:122px;top:327px;width:360px;font-size:11px;line-height:15px;color:var(--white)}

/* about */
.label{font-size:19px;color:var(--rose-label);display:flex;align-items:center;gap:10px}
.label::after{content:"";width:66px;height:3px;background:var(--rose-label)}
.h2{font-size:34px;line-height:44px;font-weight:400;color:var(--ink)}
.body-text{font-size:11px;line-height:18.5px;color:var(--muted)}
.frame{position:absolute;border:5px solid var(--navy)}

/* stats */
.stats{left:0;top:1440px;width:1200px;height:256px;background:var(--rose)}
.stat{position:absolute;top:1502px;width:124px;height:110px;border:3px solid var(--white);border-left:none;border-bottom:none}
.stat-box{position:absolute;inset:0}
.stat-num{position:absolute;left:0;right:0;bottom:2px;text-align:center;font-size:40px;font-weight:400;color:var(--white)}
.stat-label{position:absolute;top:1622px;width:170px;text-align:center;font-size:17px;color:var(--white);letter-spacing:.5px}
.divider-v{position:absolute;width:1px;background:rgba(255,255,255,.45)}

/* projects */
.projects{left:0;top:1696px;width:1200px;height:680px;background:var(--mist)}
.card{position:absolute;width:303px;height:219px;overflow:hidden}
.card .cap{position:absolute;left:0;bottom:0;width:289px;height:60px;background:var(--white);padding:8px 12px}
.cap h4{font-size:14px;font-weight:400;color:var(--ink)}
.cap p{font-size:10px;line-height:13px;color:var(--muted);margin-top:2px}
.cap svg{position:absolute;right:4px;bottom:4px}

/* contact */
.field{position:absolute;left:723px;width:353px;border:1.5px solid var(--line);font-size:11px;color:var(--ink);padding:10px 11px}

/* news */
.news{position:absolute;width:467px;height:301px}
.news .cap{position:absolute;left:0;bottom:0;width:304px;height:62px;background:var(--white);padding:10px 17px}
.news .date{font-size:11px;color:#2e4a86;text-decoration:underline}
.news h4{font-size:15px;font-weight:400;margin-top:4px}

/* cta */
.cta{left:0;top:3283px;width:1200px;height:261px;background:var(--rose)}
.cta h2{position:absolute;left:0;right:0;top:42px;text-align:center;color:var(--white);font-weight:400;font-size:34px;line-height:40px}
.cta p{position:absolute;left:350px;right:350px;top:132px;text-align:center;color:var(--white);font-size:11px;line-height:16px}

/* footer */
.footer{left:0;top:3544px;width:1200px;height:211px;background:var(--navy-deep);color:var(--white)}
.f-head{position:absolute;top:28px;font-size:15px;letter-spacing:.5px}
.f-links{position:absolute;top:66px;font-size:9px;line-height:21px}
.f-row{position:absolute;display:flex;align-items:center;gap:10px;font-size:9px;line-height:12px}
.f-ico{width:19px;height:19px;border:1px solid var(--white);border-radius:50%;flex:none}
.f-div{position:absolute;top:26px;width:1px;height:152px;background:rgba(255,255,255,.35)}
.copy{position:absolute;left:0;right:0;bottom:6px;text-align:center;font-size:8px;opacity:.85}
</style>
</head>
<body>

<!-- hero -->
<div class="abs hero" role="img" aria-label="Modern multi-family apartment buildings with wood and dark facades along a paved courtyard"></div>
<div class="abs hero-shade"></div>
<div class="abs logo" style="left:121px;top:22px"><span class="logo-mark"></span>Mireval Stone Development</div>
<nav class="abs nav"><span class="active">Home</span><span>About Us</span><span>Projects</span><span>News</span></nav>
<div class="btn contact-btn">Contact Us</div>
<div class="abs welcome">Welcome To</div>
<h1 class="abs hero-title">Mireval Stone<br>Development</h1>
<p class="abs hero-text">Lorem ipsum dolor sit amet, consectetur adipiscing elit, sed do eiusmod tempor incididunt ut labore et dolore magna aliqua.</p>
<div class="btn sand" style="left:122px;top:373px;width:108px;height:32px">Get Started</div>

<!-- about -->
<div class="abs label" style="left:118px;top:622px">About Us</div>
<h2 class="abs h2" style="left:118px;top:647px">Committed to the<br>fundamentals of Investing,<br>to ensure longterm growth</h2>
<p class="abs body-text" style="left:118px;top:786px;width:386px">Mireval Stone Development was created to satisfy the overwhelming request to help our clients who want to invest in long term buy and hold Real Estate, and create a more profitable and balanced investment portfolio. We offer opportunities to invest in cash flowing Multi-Family apartment building investments in the Southern California area.</p>
<div class="btn" style="left:118px;top:911px;width:112px;height:35px">Read More</div>
<div class="frame" style="left:679px;top:614px;width:398px;height:356px;border-right:none;border-bottom-color:var(--navy)"></div>
<div class="abs" style="left:1072px;top:740px;width:5px;height:230px;background:var(--navy)"></div>
<div class="photo" style="left:695px;top:631px;width:365px;height:323px;background:linear-gradient(160deg,#6fb0d8,#3f7ea8 45%,#5d8a4a 85%)" role="img" aria-label="Glass office towers with potted plants and a rising growth arrow"></div>
<div class="abs" style="left:1060px;top:614px;width:17px;height:5px;background:var(--navy)"></div>

<!-- section 2 -->
<div class="photo" style="left:121px;top:1038px;width:550px;height:338px;background:linear-gradient(90deg,#c8c8cc,#b88e7c 40%,#a9b5c5 75%,#e3e6ea)" role="img" aria-label="Engineer in a hard hat reviewing a tablet beside an apartment building"></div>
<h2 class="abs h2" style="left:751px;top:1060px;line-height:44px">Committed to the<br>fundamentals of<br>Investing, to ensure<br>longterm growth</h2>
<div class="abs" style="left:752px;top:1258px;font-size:44px;font-weight:300;color:transparent;-webkit-text-stroke:1px #9aa0a8">01</div>
<div class="abs" style="left:811px;top:1262px;font-size:19px;line-height:23px;color:var(--ink)">Apartment Building<br>Optimization</div>
<svg class="abs" style="left:756px;top:1335px" width="70" height="24" viewBox="0 0 70 24">
  <circle cx="12" cy="12" r="11" fill="#8e9198"/><circle cx="58" cy="12" r="11" fill="#8e9198"/>
  <path d="M6 12H40M6 12l5-4M6 12l5 4M30 12H64M64 12l-5-4M64 12l-5 4" stroke="#1f2531" stroke-width="1.6" fill="none"/>
</svg>

<!-- stats -->
<div class="abs stats"></div>
<div class="stat" style="left:121px"><svg class="stat-box" width="124" height="110"><path d="M1 110V1H124M1 110H124" stroke="#fff" stroke-width="3" fill="none"/></svg><svg class="abs" style="left:42px;top:10px" width="40" height="36" viewBox="0 0 40 36"><path d="M4 22l10-12 8 4 8-6 6 8-12 14-8-6z" fill="none" stroke="#fff" stroke-width="1.6"/></svg><div class="stat-num">02</div></div>
<div class="stat" style="left:401px"><svg class="stat-box" width="124" height="110"><path d="M1 110V1H124M1 110H124" stroke="#fff" stroke-width="3" fill="none"/></svg><svg class="abs" style="left:42px;top:10px" width="40" height="36" viewBox="0 0 40 36"><circle cx="20" cy="10" r="5" fill="none" stroke="#fff" stroke-width="1.6"/><path d="M8 34V22l6-6h12l6 6v12" fill="none" stroke="#fff" stroke-width="1.6"/></svg><div class="stat-num">06</div></div>
<div class="stat" style="left:681px"><svg class="stat-box" width="124" height="110"><path d="M1 110V1H124M1 110H124" stroke="#fff" stroke-width="3" fill="none"/></svg><svg class="abs" style="left:42px;top:8px" width="40" height="40" viewBox="0 0 40 40"><path d="M6 36V12h10v24M16 36V4h10v32M4 36h32" fill="none" stroke="#fff" stroke-width="1.6"/><circle cx="30" cy="26" r="6" fill="none" stroke="#fff" stroke-width="1.6"/></svg><div class="stat-num">33</div></div>
<div class="stat" style="left:954px"><svg class="stat-box" width="124" height="110"><path d="M1 110V1H124M1 110H124" stroke="#fff" stroke-width="3" fill="none"/></svg><svg class="abs" style="left:42px;top:8px" width="40" height="40" viewBox="0 0 40 40"><path d="M12 4h16v10a8 8 0 0 1-16 0zM20 22v8M12 34h16v4H12z" fill="none" stroke="#fff" stroke-width="1.6"/></svg><div class="stat-num">100%</div></div>
<div class="stat-label" style="left:98px">Partners</div>
<div class="stat-label" style="left:378px">Employees</div>
<div class="stat-label" style="left:658px">Investments</div>
<div class="stat-label" style="left:931px">Success</div>
<div class="divider-v" style="left:330px;top:1508px;height:112px"></div>
<div class="divider-v" style="left:599px;top:1508px;height:112px"></div>
<div class="divider-v" style="left:875px;top:1508px;height:112px"></div>

<!-- projects -->
<div class="abs projects"></div>
<h2 class="abs" style="left:0;right:0;top:1738px;text-align:center;font-size:34px;font-weight:400">Our Projects</h2>

<div class="card" style="left:124px;top:1805px"><div class="photo" style="inset:0;background:linear-gradient(180deg,#9fb8d0,#d8d6d0 55%,#7a6a54)" role="img" aria-label="Terraced apartment complex with playground"></div><div class="cap"><h4>Projects 1</h4><p>Our mixed-use developments for<br>communities to live, work &amp; play</p></div><svg class="abs" style="right:0;bottom:0" width="44" height="30"><path d="M44 0V30H0z" fill="#252c3a"/><path d="M20 22h16M31 18l5 4-5 4" stroke="#fff" stroke-width="1.4" fill="none"/></svg></div>
<div class="card" style="left:448px;top:1805px"><div class="photo" style="inset:0;background:linear-gradient(180deg,#b6c3cf,#8a9aa6 55%,#5e7454)" role="img" aria-label="Residential towers with a landscaped podium"></div><div class="cap"><h4>Projects 2</h4><p>Our mixed-use developments for<br>communities to live, work &amp; play</p></div><svg class="abs" style="right:0;bottom:0" width="44" height="30"><path d="M44 0V30H0z" fill="#252c3a"/><path d="M20 22h16M31 18l5 4-5 4" stroke="#fff" stroke-width="1.4" fill="none"/></svg></div>
<div class="card" style="left:773px;top:1805px"><div class="photo" style="inset:0;background:linear-gradient(90deg,#9b6a45,#e8e4dc 35%,#c99a6c 70%,#1c2430)" role="img" aria-label="Modern apartment kitchen with wood ceiling"></div><div class="cap"><h4>Projects 3</h4><p>Our mixed-use developments for<br>communities to live, work &amp; play</p></div><svg class="abs" style="right:0;bottom:0" width="44" height="30"><path d="M44 0V30H0z" fill="#252c3a"/><path d="M20 22h16M31 18l5 4-5 4" stroke="#fff" stroke-width="1.4" fill="none"/></svg></div>
<div class="card" style="left:124px;top:2044px"><div class="photo" style="inset:0;background:linear-gradient(180deg,#8a6446,#ecebe8 30%,#d4d2cd)" role="img" aria-label="Bright open-plan living room"></div><div class="cap"><h4>Projects 4</h4><p>Our mixed-use developments for<br>communities to live, work &amp; play</p></div><svg class="abs" style="right:0;bottom:0" width="44" height="30"><path d="M44 0V30H0z" fill="#252c3a"/><path d="M20 22h16M31 18l5 4-5 4" stroke="#fff" stroke-width="1.4" fill="none"/></svg></div>
<div class="card" style="left:448px;top:2044px"><div class="photo" style="inset:0;background:linear-gradient(180deg,#1f3f86,#2a3550 45%,#2b2a2c)" role="img" aria-label="Modern home facade at dusk"></div><div class="cap"><h4>Projects 5</h4><p>Our mixed-use developments for<br>communities to live, work &amp; play</p></div><svg class="abs" style="right:0;bottom:0" width="44" height="30"><path d="M44 0V30H0z" fill="#252c3a"/><path d="M20 22h16M31 18l5 4-5 4" stroke="#fff" stroke-width="1.4" fill="none"/></svg></div>
<div class="card" style="left:773px;top:2044px"><div class="photo" style="inset:0;background:linear-gradient(180deg,#24428a,#5a5048 45%,#2c2a2a)" role="img" aria-label="Modern house with glass garage and lit steps at dusk"></div><div class="cap"><h4>Projects 6</h4><p>Our mixed-use developments for<br>communities to live, work &amp; play</p></div><svg class="abs" style="right:0;bottom:0" width="44" height="30"><path d="M44 0V30H0z" fill="#252c3a"/><path d="M20 22h16M31 18l5 4-5 4" stroke="#fff" stroke-width="1.4" fill="none"/></svg></div>
<div class="btn" style="left:532px;top:2290px;width:134px;height:36px">View All Project</div>

<!-- contact -->
<div class="frame" style="left:121px;top:2442px;width:491px;height:362px;border-right:none;border-top-width:5px"></div>
<div class="abs" style="left:607px;top:2615px;width:5px;height:189px;background:var(--navy)"></div>
<div class="photo" style="left:143px;top:2463px;width:450px;height:322px;background:linear-gradient(135deg,#b9c9c7,#e7ecea 50%,#8a9596)" role="img" aria-label="Hands sketching plans on paper beside a laptop"></div>
<h2 class="abs" style="left:720px;top:2449px;font-size:33px;line-height:43px;font-weight:400">For any inquiries,<br>please call or email us.</h2>
<p class="abs" style="left:723px;top:2541px;font-size:12px;color:var(--muted)">Alternatively you can fill in the following contact form.</p>
<div class="field" style="top:2575px;height:35px">Name</div>
<div class="field" style="top:2623px;height:35px">Email</div>
<div class="field" style="top:2671px;height:75px">Message</div>
<div class="btn" style="left:725px;top:2761px;width:92px;height:30px">Submit</div>

<!-- news -->
<h2 class="abs" style="left:121px;top:2851px;font-size:32px;font-weight:400">Latest News</h2>
<div class="btn" style="left:940px;top:2853px;width:136px;height:35px">View All News</div>
<div class="news" style="left:122px;top:2920px"><div class="photo" style="inset:0;background:linear-gradient(180deg,#1f4194,#4a4d55 50%,#2e2a28)" role="img" aria-label="Modern home with patio lounge seating at dusk"></div><div class="cap"><span class="date">Feb 20, 2022</span><h4>Bold and Breathtaking</h4></div></div>
<div class="news" style="left:611px;top:2920px"><div class="photo" style="inset:0;background:linear-gradient(90deg,#9a6a45,#ebe8e2 35%,#c9975f 65%,#1a2230)" role="img" aria-label="Modern kitchen interior with wood ceiling and dark screen wall"></div><div class="cap"><span class="date">Feb 20, 2022</span><h4>Bold and Breathtaking</h4></div></div>

<!-- cta -->
<div class="abs cta">
  <h2>Start Your New Journey<br>with Mireval Stone Development</h2>
  <p>Lorem ipsum dolor sit amet, consectetur adipiscing elit, sed do eiusmod tempor incididunt ut labore et dolore magna aliqua. Quis ipsum suspendisse ultrices gravida.</p>
</div>
<div class="btn light" style="left:510px;top:3455px;width:178px;height:34px;font-size:11px">Start Your Journey</div>

<!-- footer -->
<footer class="abs footer">
  <div class="abs logo" style="left:121px;top:30px;font-size:15px"><span class="logo-mark" style="width:24px;height:24px"></span>Mireval Stone Development</div>
  <p class="abs" style="left:122px;top:70px;width:225px;font-size:9px;line-height:18px">Mireval Stone Development was created to satisfy the overwhelming request to help our clients who want to invest in long term buy and hold Real Estate, and create a more profitable and balanced investment portfolio.</p>
  <div class="f-div" style="left:389px"></div>
  <div class="f-head" style="left:478px">About Us</div>
  <div class="f-links" style="left:478px">Home<br>About Us<br>Projects<br>News<br>Contact Us</div>
  <div class="f-div" style="left:633px"></div>
  <div class="f-head" style="left:700px">Contact Us</div>
  <div class="f-row" style="left:701px;top:66px"><span class="f-ico"></span>1840 Larkfield Ave Suite 310<br>Coralview, CA. 90412</div>
  <div class="f-row" style="left:701px;top:101px"><span class="f-ico"></span>hello@mirevalstonedev.com</div>
  <div class="f-row" style="left:701px;top:133px"><span class="f-ico"></span>+ (555) 204-3817</div>
  <div class="f-div" style="left:962px"></div>
  <div class="f-head" style="left:996px">Follow Us</div>
  <div class="f-row" style="left:997px;top:66px"><span class="f-ico"></span>Friendsphere</div>
  <div class="f-row" style="left:997px;top:97px"><span class="f-ico"></span>Careerlink</div>
  <div class="f-row" style="left:997px;top:128px"><span class="f-ico"></span>Chirpline</div>
  <div class="copy">© 2024 Mireval Stone Development All Rights Reserved</div>
</footer>

</body>
</html>
```